Thriving Mexican import business needs a new business card

Need a refresher of our current business card. Looking for a lighter background with the logo on one side. We will want this file to be adjustable so we can change names, emails and mobile numbers.
We are open to ideas but maintaining a professional image is critical.
Thankyou,

Target Market(s)

Anyone in food industry

Industry/Entity Type

Wholesale

Contact Information for Business Card

Mark Pendlebury
Director
Condor Provisions & Spirits Pty Ltd
5B Morrow Ct, Kelvinbrook VIC 3127
0421930576 (03) 95128460
mark@condorlatino.example.au
condorlatinoprovisionsandspirits.example.au

Font styles to use
Serif
Other font styles liked:
• NeoGram Heavy

Requirements
Must have
• Professional yet memorable
Condor logo
Nice to have
• Chilli or tequila/mexican food pictures
Should not have
• Dark background

```html
<!DOCTYPE html>
<html lang="en">
<head>
<meta charset="utf-8">
<title>Condor Provisions &amp; Spirits – Business Card</title>
<link rel="stylesheet" href="https://fonts.googleapis.com/css2?family=Oswald:wght@600&family=Montserrat:wght@600;700&family=Roboto+Condensed:wght@400&display=swap">
<style>
  :root {
    --terracotta: #cf6a3d;
    --terracotta-deep: #b85a31;
    --terracotta-light: #d9784a;
    --ink: #141414;
    --paper: #ffffff;
    --stage: #ececec;
  }
  html, body {
    margin: 0;
    width: 1200px;
    height: 900px;
    overflow: hidden;
    background: var(--stage);
  }
  .stage {
    position: relative;
    width: 1200px;
    height: 900px;
  }
  .card {
    position: absolute;
    left: 300px;
    width: 600px;
    height: 343px;
    overflow: hidden;
    box-shadow: 0 6px 18px rgba(0,0,0,0.18);
  }
  /* Front */
  .card-front {
    top: 70px;
    background: var(--terracotta);
  }
  .front-decoration {
    position: absolute;
    inset: 40px 20px 30px 20px;
    border-radius: 30px;
    background: linear-gradient(160deg, var(--terracotta-light) 0%, var(--terracotta-deep) 100%);
    opacity: 0.45;
  }
  .front-brand {
    position: absolute;
    left: 0; right: 0;
    top: 118px;
    display: flex;
    align-items: center;
    justify-content: center;
    gap: 16px;
  }
  .brand-square {
    width: 34px;
    height: 34px;
    border: 3px solid var(--paper);
    box-sizing: border-box;
    flex: none;
  }
  .front-brand .brand-name {
    font-family: "Oswald", sans-serif;
    font-weight: 600;
    font-size: 84px;
    line-height: 1;
    letter-spacing: 1px;
    color: var(--paper);
  }
  /* Back */
  .card-back {
    top: 487px;
    background: var(--paper);
  }
  .back-header {
    position: absolute;
    left: 150px;
    right: 30px;
    top: 28px;
    display: flex;
    align-items: center;
    gap: 12px;
  }
  .back-header .brand-square {
    border-color: var(--ink);
    width: 26px;
    height: 26px;
  }
  .back-header .brand-name {
    font-family: "Oswald", sans-serif;
    font-weight: 600;
    font-size: 58px;
    line-height: 1;
    color: var(--ink);
    flex: none;
  }
  .rule {
    height: 1.5px;
    background: var(--terracotta);
  }
  .rule-top {
    flex: 1;
    margin-left: 18px;
  }
  .rule-bottom {
    position: absolute;
    left: 30px;
    width: 300px;
    top: 258px;
  }
  .holder {
    position: absolute;
    right: 318px;
    top: 176px;
    text-align: right;
  }
  .holder-name {
    font-family: "Montserrat", sans-serif;
    font-weight: 700;
    font-size: 21px;
    color: var(--terracotta);
    text-transform: uppercase;
    letter-spacing: 0.5px;
  }
  .holder-role {
    font-family: "Roboto Condensed", sans-serif;
    font-size: 14px;
    color: var(--ink);
    margin-top: 2px;
  }
  .divider {
    position: absolute;
    left: 294px;
    top: 150px;
    width: 1px;
    height: 70px;
    background: var(--ink);
  }
  .contacts {
    position: absolute;
    left: 306px;
    top: 148px;
    margin: 0;
    padding: 0;
    list-style: none;
    font-family: "Roboto Condensed", sans-serif;
    font-size: 13.5px;
    color: var(--ink);
  }
  .contacts li {
    display: flex;
    align-items: center;
    gap: 8px;
    height: 23px;
  }
  .contacts svg { width: 13px; height: 13px; flex: none; }
  .sep { color: var(--terracotta); padding: 0 3px; }
  .address {
    position: absolute;
    right: 30px;
    bottom: 36px;
    font-family: "Roboto Condensed", sans-serif;
    font-size: 14px;
    color: var(--ink);
  }
</style>
</head>
<body>
<main class="stage">
  <section class="card card-front">
    <div class="front-decoration" role="img" aria-label="Faint tonal illustration of a Mexican knife and chilli across the card"></div>
    <div class="front-brand">
      <span class="brand-square"></span>
      <span class="brand-name">CONDOR</span>
    </div>
  </section>

  <section class="card card-back">
    <div class="back-header">
      <span class="brand-square"></span>
      <span class="brand-name">CONDOR</span>
      <span class="rule rule-top"></span>
    </div>

    <div class="holder">
      <div class="holder-name">Mark Pendlebury</div>
      <div class="holder-role">Director</div>
    </div>
    <div class="divider"></div>

    <ul class="contacts">
      <li>
        <svg viewBox="0 0 16 16" fill="none" stroke="var(--terracotta)" stroke-width="1.4"><circle cx="8" cy="8" r="7"/><path d="M5.5 4.5l1.5 1.5-1 1a5 5 0 0 0 3 3l1-1 1.5 1.5-1 1.2c-3 0-6-3-6-6z"/></svg>
        <span>0421 930 576<span class="sep">|</span>(03) 9512 8460</span>
      </li>
      <li>
        <svg viewBox="0 0 16 16" fill="none" stroke="var(--terracotta)" stroke-width="1.4"><rect x="1.5" y="3.5" width="13" height="9"/><path d="M1.5 3.5l6.5 5 6.5-5"/></svg>
        <span>mark@condorlatino.example.au</span>
      </li>
      <li>
        <svg viewBox="0 0 16 16" fill="none" stroke="var(--terracotta)" stroke-width="1.3"><circle cx="8" cy="8" r="6.5"/><ellipse cx="8" cy="8" rx="3" ry="6.5"/><path d="M1.5 8h13"/></svg>
        <span>condorlatinoprovisionsandspirits.example.au</span>
      </li>
    </ul>

    <div class="rule rule-bottom"></div>
    <div class="address">5B Morrow Ct, Kelvinbrook VIC 3127</div>
  </section>
</main>
</body>
</html>
```